Theatre Poster Design/Key Art Project

I need key art that can be used in a variety of iterations to promote a theatrical production of Lucas Emory Finch’s adaptation of MARGIT SOLVANG by Osvald Kremer. This is a landmark work of drama that takes place in the very late 19th Century. For more information, consult http://en.lorevault-archive.org/wiki/Margit_Solvang

“Returning from their honeymoon, Anton and Margit Rydell begin to settle into their new life together. With the return of Sigurd Halvik, Anton’s academic nemesis, the couple’s relationship unravels amidst whispered secrets, professional disappointments, and a startling realization of what life truly holds for Margit as Anton’s wife. Passion and rivalries flare in this new adaptation by Lucas Emory Finch, who breathes new life into Kremer’s classic tale with an interpretation of Margit unlike any other.”

While the initial project is an 11"x17" poster, I need the essential design elements to be able to be replicated on a direct mail card, in email blitzes, etc.

This is a serious drama. We would like a highly graphic poster that does not attempt to tell the story.

Reason: We ran out of time and were unable to provide feedback. Things around here are very busy. We'd like to extend this contest to hopefully get a few more designs and provide feedback in the next day or two to those designs that we are considering as of now.

I want to try to get darker in terms of the design. Something that is going to be more compelling to our average patron. Can we play with the cleaning of the pistol.It is clear in the script that Margit loves her guns and would care greatly for them, so I want to play with the guns and the accessories that may go along with the guns of the period.

Target Market(s)

university students ages 18-22
theatre patrons ages 35-80

Industry/Entity Type

Work

Requirements
Must have
• must use the KPD Theatre logo
Should not have
• tragedy/comedy masks

```html
<!DOCTYPE html>
<html lang="en">
<head>
<meta charset="utf-8">
<title>Margit Solvang — KPD Theatre &amp; Dance</title>
<link rel="stylesheet" href="https://fonts.googleapis.com/css2?family=Cinzel:wght@700;900&family=Federant&display=swap">
<style>
  :root {
    --ink: #050505;
    --paper: #ffffff;
    --red: #ff1a12;
    --red-deep: #b80d08;
    --grey-mid: #6f6f6f;
    --grey-dark: #1b1b1b;
  }
  * { margin: 0; padding: 0; box-sizing: border-box; }
  html, body { width: 776px; height: 1200px; overflow: hidden; background: var(--ink); }
  .poster {
    position: relative;
    width: 776px;
    height: 1200px;
    overflow: hidden;
    background: var(--ink);
    font-family: "Cinzel", Georgia, serif;
    color: var(--paper);
  }
  .key-art {
    position: absolute;
    inset: 0;
    background:
      radial-gradient(ellipse 210px 250px at 388px 330px, #cfcfcf 0%, #8a8a8a 45%, rgba(20,20,20,0) 100%),
      radial-gradient(ellipse 360px 360px at 388px 300px, #2a2a2a 0%, #121212 70%, rgba(0,0,0,0) 100%),
      linear-gradient(180deg, #0a0a0a 0%, #111 45%, #3a3a3a 68%, #5a5a5a 76%, #2a2a2a 88%, #080808 100%);
  }
  .company {
    position: absolute;
    top: 14px;
    left: 0;
    width: 100%;
    text-align: center;
    font-weight: 700;
    color: var(--paper);
  }
  .company-name { font-size: 36px; letter-spacing: 0.5px; line-height: 44px; }
  .company-school { font-size: 17px; letter-spacing: 0.5px; line-height: 22px; }
  .presents {
    position: absolute;
    top: 114px;
    left: 0;
    width: 100%;
    text-align: center;
    font-size: 19px;
    font-weight: 900;
    letter-spacing: 14px;
    padding-left: 14px;
  }
  .title {
    position: absolute;
    left: 0;
    top: 570px;
    width: 776px;
    height: 350px;
  }
  .title text { font-family: "Federant", "Cinzel", serif; font-size: 172px; }
  .credits {
    position: absolute;
    top: 926px;
    left: 0;
    width: 100%;
    text-align: center;
    font-weight: 900;
    line-height: 40px;
  }
  .credits .author { font-size: 31px; }
  .credits .adapter { font-size: 29px; }
  .run-info {
    position: absolute;
    top: 1064px;
    left: 0;
    width: 100%;
    text-align: center;
    font-family: "Federant", "Cinzel", serif;
  }
  .run-tagline { color: var(--red); font-size: 30px; line-height: 40px; letter-spacing: 1px; }
  .run-details { font-size: 24px; line-height: 36px; letter-spacing: 0.5px; }
  .run-contact { font-size: 24px; line-height: 34px; letter-spacing: 0.5px; }
  .run-contact .web { color: var(--red); }
</style>
</head>
<body>
<main class="poster">
  <div class="key-art" role="img" aria-label="Black and white photograph of a woman with a dark curly halo of hair, eyes closed and vivid red lips, fading down into a misty wooden pier"></div>

  <header class="company">
    <div class="company-name">KPD Theatre &amp; Dance</div>
    <div class="company-school">Kestrel Point University</div>
  </header>
  <p class="presents">PRESENTS</p>

  <svg class="title" viewBox="0 0 776 350" aria-label="Margit Solvang">
    <defs>
      <linearGradient id="title-red" x1="0" y1="0" x2="0" y2="1">
        <stop offset="0" stop-color="var(--red)"/>
        <stop offset="0.7" stop-color="var(--red)"/>
        <stop offset="1" stop-color="var(--red-deep)"/>
      </linearGradient>
    </defs>
    <text x="92" y="150" textLength="596" lengthAdjust="spacingAndGlyphs" fill="url(#title-red)">MARGIT</text>
    <text x="80" y="330" textLength="648" lengthAdjust="spacingAndGlyphs" fill="url(#title-red)">SOLVANG</text>
  </svg>

  <section class="credits">
    <div class="author">BY OSVALD KREMER</div>
    <div class="adapter">ADAPTED BY LUCAS EMORY FINCH</div>
  </section>

  <footer class="run-info">
    <div class="run-tagline">TWO WEEKS ONLY!</div>
    <div class="run-details">APRIL 12-22 | HARLOW THEATRE | TICKETS $6-$14</div>
    <div class="run-contact">555-010-2244 | <span class="web">KPD.TIX-EXAMPLE.COM</span></div>
  </footer>
</main>
</body>
</html>
```